WP website design Pine Harbor (Contest)

We need a wordpress design that will incorporate a professional color scheme with company logo in a clean layout. The design needs to consider that this will be developed on a responsive theme. Colors are blue and green of the logo and and an accent color (perhaps very light brown/tan). Client wants a 'modern' look.

Industry/Entity Type

It Company

Font styles to use
Serif
Sans Serif

Colors

Designer to choose colors to be used in the design.

Requirements
Must have
• Navigation: 1) Home; 2) Upcoming Auctions; 3) Past Auctions; 4) About Us; 5) Services; 6) Sellers; 7) Buyers; 8) Contact Us

Site will have slideshow - image is attached. Colors will be those in the logo, blue and green with maybe an accent color. A site the client mentions liking is pineharborauctions.net for the use of color and layout.

Widgets: 1) Featured Properties; 2) Call to action for Sellers 3) Testimonials blog/widget
Nice to have
• use of dropdown menus

```html
<!DOCTYPE html>
<html lang="en">
<head>
<meta charset="utf-8">
<title>Pine Harbor – Hale Brandt Auction Marketing</title>
<link href="https://fonts.googleapis.com/css2?family=Open+Sans:wght@400;600;700;800&display=swap" rel="stylesheet">
<style>
:root{
  --blue:#1f60ad;
  --blue-dark:#0f3f7c;
  --blue-band:#1a5398;
  --green:#2f8a3f;
  --green-dark:#1d6a2e;
  --grey-bg:#ececec;
  --text:#444;
  --muted:#777;
  --white:#fff;
  --photo-a:#8a99a8;
  --photo-b:#c7cfd6;
}
*{box-sizing:border-box;margin:0;padding:0}
html,body{width:1200px;height:2328px;overflow:hidden}
body{font-family:"Open Sans",Arial,sans-serif;color:var(--text);
  background:linear-gradient(180deg,var(--green-dark) 0,var(--green) 230px,#dfe6df 320px,#f2f2f2 420px,#f2f2f2 100%);position:relative}
.page{position:absolute;left:152px;top:20px;width:896px;height:2308px;background:var(--white)}
.abs{position:absolute}
.photo{background:linear-gradient(135deg,var(--photo-a),var(--photo-b))}

/* header */
.site-header{left:0;top:0;width:896px;height:120px}
.brand{left:22px;top:26px;display:flex;align-items:center;gap:12px}
.brand-mark{width:22px;height:22px;background:var(--green)}
.brand-name{font-weight:800;font-size:28px;color:var(--blue);line-height:1}
.brand-sub{left:56px;top:62px;font-size:12px;font-weight:700;color:var(--blue-dark);letter-spacing:.5px}
.header-contact{right:24px;top:26px;display:flex;gap:18px;align-items:flex-start}
.social{display:flex;gap:6px}
.social span{width:22px;height:22px;border-radius:50%;background:var(--blue)}
.social span:nth-child(2){background:#3a8fd6}
.social span:nth-child(3){background:#c8312a}
.contact-lines{font-size:12px;line-height:20px;color:var(--text)}

/* nav */
.main-nav{left:0;top:120px;width:896px;height:40px;background:var(--blue);display:flex;padding-left:20px;border-bottom:3px solid var(--blue-dark)}
.main-nav a{color:var(--white);font-size:13px;font-weight:700;text-decoration:none;padding:0 19px;line-height:38px}
.main-nav a.active{background:var(--blue-dark)}

/* hero */
.hero{left:0;top:160px;width:896px;height:360px;background:linear-gradient(120deg,#6f7f8f,#b9c3cc 45%,#8f9ca8)}
.hero-caption{left:548px;top:196px;width:320px;padding:14px 18px;background:rgba(15,63,124,.85);color:var(--white)}
.hero-caption h2{font-size:22px;font-weight:700;line-height:28px}
.btn{display:inline-block;background:var(--blue);color:var(--white);font-size:11px;font-weight:700;padding:6px 14px;border-radius:2px}
.hero-caption .btn{margin-top:10px;background:var(--blue)}
.dots{left:0;top:532px;width:896px;display:flex;justify-content:center;gap:8px}
.dots span{width:9px;height:9px;border-radius:50%;background:#888}
.dots span:first-child{background:var(--blue)}

.tagline{left:118px;top:558px;width:660px;text-align:center;font-size:13px;line-height:22px;color:var(--text)}
.tagline b{color:var(--blue)}

/* upcoming + services */
.upcoming{left:20px;top:632px;width:244px;height:440px;background:linear-gradient(180deg,var(--blue),var(--blue-dark));color:var(--white);padding:18px}
.upcoming h3{font-size:26px;font-weight:800;line-height:30px}
.upcoming .sub{font-size:12px;font-weight:700;margin-top:8px;line-height:17px}
.upcoming .thumb{width:208px;height:100px;margin:14px 0}
.upcoming .meta{font-size:11px;line-height:16px}
.upcoming .btn{margin-top:22px;background:var(--blue-dark);border:1px solid #5b8fd0}
.tile{width:292px;height:212px;background:var(--blue);padding:6px}
.tile-head{height:36px;display:flex;align-items:center;justify-content:space-between;color:var(--white);font-size:12px;font-weight:700;padding:0 6px;line-height:15px}
.tile-head .btn{background:var(--blue-dark);font-size:10px;padding:4px 10px;flex:none}
.tile .photo{height:164px}
.sublinks{left:0;top:1092px;width:896px;text-align:center;font-size:10px;color:var(--muted)}

/* featured auctions */
.featured{left:0;top:1140px;width:896px;height:400px;background:var(--blue-band)}
.featured h3{position:absolute;left:0;top:26px;width:896px;text-align:center;color:var(--white);font-size:20px;font-weight:700}
.card{width:196px;top:80px;color:var(--white)}
.card .photo{height:110px}
.card .title{font-size:11px;font-weight:600;line-height:15px;margin-top:10px}
.card .kind{font-size:11px;font-weight:700;margin-top:6px}
.card .note{font-size:10px;line-height:14px;margin-top:14px}
.card .actions{display:flex;gap:4px;margin-top:22px}
.card .actions span{flex:1;background:var(--white);color:var(--blue-dark);font-size:9px;font-weight:700;text-align:center;line-height:20px}

/* video + news */
.section-title{font-size:18px;font-weight:700;color:var(--blue);padding-bottom:6px;border-bottom:2px solid var(--green)}
.video{left:20px;top:1580px;width:468px}
.video .photo{height:330px;margin-top:16px;background:linear-gradient(180deg,#4b78b8,#9fc0e2 55%,#3c4d63)}
.news{left:528px;top:1580px;width:348px}
.news-item{display:flex;gap:12px;margin-top:16px}
.news-item .photo{width:86px;height:68px;flex:none}
.news-item .date{font-size:11px;font-weight:700;color:var(--blue)}
.news-item p{font-size:10px;line-height:13px;color:var(--text)}
.news-item .btn{margin-top:3px;background:var(--green);font-size:9px;padding:2px 8px}

/* footer */
.site-footer{left:0;top:1990px;width:896px;height:318px;background:var(--grey-bg)}
.signup{left:20px;top:20px;width:856px;display:flex;align-items:center;gap:14px;font-size:11px;font-weight:700;color:var(--blue-dark);border-bottom:1px solid #d2d2d2;padding-bottom:14px}
.signup .ico{width:16px;height:12px;background:var(--green)}
.signup .field{margin-left:26px;width:330px;height:26px;background:var(--white);border:1px solid #ccc;font-weight:400;color:var(--muted);padding:0 8px;line-height:24px}
.signup .btn{margin-left:auto;background:var(--blue-dark);padding:6px 26px}
.foot-brand{left:40px;top:84px}
.foot-brand .brand-name{font-size:20px}
.foot-links{left:250px;top:80px;font-size:11px;line-height:19px}
.foot-contact{left:430px;top:80px;font-size:11px;line-height:19px}
.badges{left:700px;top:84px;display:flex;gap:8px}
.badges span{width:34px;height:30px;background:#bdbdbd}
.badges span:nth-child(2){background:#9e9e9e}
.badges span:nth-child(3){width:44px;background:#8d8d8d}
.foot-social{left:704px;top:150px}
.copyright{left:0;top:288px;width:896px;text-align:center;font-size:10px;color:var(--muted)}
</style>
</head>
<body>
<div class="page">

  <header class="site-header abs">
    <div class="brand abs"><span class="brand-mark"></span><span class="brand-name">Pine Harbor</span></div>
    <div class="brand-sub abs">Hale Brandt Auction Marketing</div>
    <div class="header-contact abs">
      <div class="social"><span></span><span></span><span></span></div>
      <div class="contact-lines">(555) 014-2290<br>info@pineharborauctions.net</div>
    </div>
  </header>

  <nav class="main-nav abs">
    <a class="active">Home</a><a>Services</a><a>Auctions by Type</a><a>About Us</a><a>SMP Report</a><a>Videos</a><a>Contact Us</a>
  </nav>

  <section class="hero abs" role="img" aria-label="Slideshow photo of an industrial plant with machinery">
    <div class="hero-caption abs">
      <h2>Making Sold Specialty<br>for 30 years</h2>
      <span class="btn">Learn More</span>
    </div>
  </section>
  <div class="dots abs"><span></span><span></span><span></span><span></span></div>

  <p class="tagline abs">The go-to business asset liquidation and real estate at auction solution provider in Texas and across the southwest for over 30 years using our proprietary SMP™ process. <b>Learn More</b></p>

  <section class="upcoming abs">
    <h3>Upcoming<br>Auctions</h3>
    <p class="sub">Appointed Assets, Harbor Bay, TX<br>Real Estate Auction</p>
    <div class="thumb photo" role="img" aria-label="Photo of the auction property"></div>
    <p class="meta">Tuesday, January 14, 2014<br>@ 12:00 PM CST<br>Appointed Assets<br>Harbor Bay, TX</p>
    <span class="btn">Read More</span>
  </section>

  <div class="tile abs" style="left:284px;top:632px"><div class="tile-head">Real Estate<span class="btn">Learn More</span></div><div class="photo" role="img" aria-label="Photo of a residential property"></div></div>
  <div class="tile abs" style="left:584px;top:632px"><div class="tile-head">Business Liquidations<span class="btn">Learn More</span></div><div class="photo" role="img" aria-label="Photo of a business meeting"></div></div>
  <div class="tile abs" style="left:284px;top:860px"><div class="tile-head"><span>Commercial Industrial<br>Equipment Auctions</span><span class="btn">Learn More</span></div><div class="photo" role="img" aria-label="Photo of industrial equipment"></div></div>
  <div class="tile abs" style="left:584px;top:860px"><div class="tile-head">Appraisals<span class="btn">Learn More</span></div><div class="photo" role="img" aria-label="Photo of an appraiser at work"></div></div>

  <p class="sublinks abs">The SMP™ Report | Regional Awards | Lifetime Achievement Award | Links to SMP Report | Former News | page</p>

  <section class="featured abs">
    <h3>Featured Auctions</h3>
    <div class="card abs" style="left:20px">
      <div class="photo" role="img" aria-label="Photo of lakefront lots"></div>
      <p class="title">4 Contiguous Lakefront Lots in Exclusive Community</p>
      <p class="kind">Sealed Bid Auction</p>
      <p class="note">Bids for Qualifying Round are due January 30 at 4PM</p>
      <div class="actions"><span>Details</span><span>Photos</span><span>Videos</span></div>
    </div>
    <div class="card abs" style="left:240px">
      <div class="photo" role="img" aria-label="Photo of a lakeside home"></div>
      <p class="title">4 Contiguous Lakefront Lots in Exclusive Community</p>
      <p class="kind">Sealed Bid Auction</p>
      <p class="note">Bids for Qualifying Round are due January 30 at 4PM</p>
      <div class="actions"><span>Details</span><span>Photos</span><span>Videos</span></div>
    </div>
    <div class="card abs" style="left:460px">
      <div class="photo" role="img" aria-label="Photo of a suburban house"></div>
      <p class="title">4 Contiguous Lakefront Lots in Exclusive Community</p>
      <p class="kind">Sealed Bid Auction</p>
      <p class="note">Bids for Qualifying Round are due January 30 at 4PM</p>
      <div class="actions"><span>Details</span><span>Photos</span><span>Videos</span></div>
    </div>
    <div class="card abs" style="left:680px">
      <div class="photo" role="img" aria-label="Photo of a family home"></div>
      <p class="title">4 Contiguous Lakefront Lots in Exclusive Community</p>
      <p class="kind">Sealed Bid Auction</p>
      <p class="note">Bids for Qualifying Round are due January 30 at 4PM</p>
      <div class="actions"><span>Details</span><span>Photos</span><span>Videos</span></div>
    </div>
  </section>

  <section class="video abs">
    <h3 class="section-title">Featured Video</h3>
    <div class="photo" role="img" aria-label="Video still of a modern glass building at dusk"></div>
  </section>

  <section class="news abs">
    <h3 class="section-title">News &amp; Events blog</h3>
    <div class="news-item"><div class="photo" role="img" aria-label="News photo"></div><div><p class="date">November, 2nd, 2014</p><p>Neque porro quisquam est qui dolorem ipsum quia dolor sit amet, consectetur, adipisci velit.</p><span class="btn">Read More</span></div></div>
    <div class="news-item"><div class="photo" role="img" aria-label="News photo"></div><div><p class="date">November, 2nd, 2014</p><p>Neque porro quisquam est qui dolorem ipsum quia dolor sit amet, consectetur, adipisci velit.</p><span class="btn">Read More</span></div></div>
    <div class="news-item"><div class="photo" role="img" aria-label="News photo"></div><div><p class="date">November, 2nd, 2014</p><p>Neque porro quisquam est qui dolorem ipsum quia dolor sit amet, consectetur, adipisci velit.</p><span class="btn">Read More</span></div></div>
    <div class="news-item"><div class="photo" role="img" aria-label="News photo"></div><div><p class="date">November, 2nd, 2014</p><p>Neque porro quisquam est qui dolorem ipsum quia dolor sit amet, consectetur, adipisci velit.</p><span class="btn">Read More</span></div></div>
  </section>

  <footer class="site-footer abs">
    <div class="signup abs"><span class="ico"></span>Sign Up For Auction Alerts<span class="field">E-Mail Address</span><span class="btn">SUBSCRIBE</span></div>
    <div class="foot-brand abs">
      <div class="brand"><span class="brand-mark" style="width:16px;height:16px"></span><span class="brand-name">Pine Harbor</span></div>
    </div>
    <div class="foot-links abs">Home<br>Services<br>Auctions by Type<br>About Us<br>SMP Report<br>Videos<br>Contact Us</div>
    <div class="foot-contact abs">Phone: (555) 014-2290<br>Mobile: (555) 014-7731<br>Email: info@pineharborauctions.net<br>auction@pineharborauctions.net<br><br>Address: 1401 Harbor Rd<br>Cedar Point, TX 78600</div>
    <div class="badges abs"><span></span><span></span><span></span></div>
    <div class="foot-social social abs"><span></span><span></span><span></span></div>
    <p class="copyright abs">© 2014 Pine Harbor. All Rights Reserved</p>
  </footer>

</div>
</body>
</html>
```